The Motion Depot needs a postcard design.

We need a postcard design for our new retail/consignment store called "The Motion Depot". We buy, sell and consign gently used exercise equipment. We offer treadmills, ellipticals, gyms, bikes and more. We can save our customers up to 50% off retail prices. We also offer delivery, set-up, removal/recycling of old equipment, and repair. Our initial product/business (and formerly store name) is RoverWorks Gym Mending - our mobile business that offers repairs & service/maintenance. We would like this postcard to focus only on The Motion Depot and be bright, colorful and cheerful, inviting the community to come in and see how we can fit them with the right piece of equipment both physically and economically.
We specialize in buying, selling and consigning pre-owned equipment.

The overall design should be informative about who we are, what we offer, and one that communicates we are inviting them to stop by and check us out.

Thank you!!

Target Market(s)

People wanting to work out at home on a budget.
The elderly, rehab patients, moms wanting pre-baby body back,
health conscience people as well as appeal the the younger crowd.

Industry/Entity Type

Fitness Equipment

Font styles to use
Serif

Colors
3276b5
33a6d7
0393ce
33b8a4
add136
fbee3d
ffcf3e
faa54b

Requirements
Must have
• our logo, address: 4871 Birchwood Ave. NE Salem, Or 97305, phone #: 971-555-0187
• lots of color-
• Caption of " Save up to 50% off of retail prices
• "We deliver" "Delivery Available"
Nice to have
• We like the design idea of layering images, transparent images in the background and the use of lots of color that engages the potential customer.
• Website or QR code - www.themotiondepot.example
Should not have
• Realistic images of people or exercise equipment. Should not be tailored after our RoverWorks website. This is a completely different business. We want to stay away from the red/black color scheme. Also should not mention "NEW". We do not want the focus to be on new equipment.

```html
<!DOCTYPE html>
<html lang="en">
<head>
<meta charset="utf-8">
<title>The Motion Depot – Postcard</title>
<link href="https://fonts.googleapis.com/css2?family=Josefin+Sans:wght@400;600;700&display=swap" rel="stylesheet">
<style>
  :root {
    --page: #e9e7e4;
    --plum-deep: #4a3157;
    --plum: #5c3d6c;
    --magenta: #c1579d;
    --pink: #d86aac;
    --teal: #6cc6bb;
    --lime: #e2dc3c;
    --ink-dark: #4a3157;
    --white: #ffffff;
  }
  * { margin: 0; padding: 0; box-sizing: border-box; }
  html, body {
    width: 1200px; height: 900px; overflow: hidden;
    background: var(--page);
    font-family: "Josefin Sans", sans-serif;
  }
  .postcard {
    position: absolute; left: 45px; top: 70px;
    width: 1110px; height: 760px;
    background: var(--plum);
    overflow: hidden;
    box-shadow: 0 10px 30px rgba(0,0,0,.18);
  }
  .backdrop-art {
    position: absolute; inset: 0;
    background:
      radial-gradient(circle at 96% 4%, var(--teal) 0, rgba(108,198,187,.7) 90px, transparent 180px),
      radial-gradient(ellipse at 22% 55%, rgba(216,106,172,.85) 0, rgba(193,87,157,.5) 220px, transparent 380px),
      radial-gradient(ellipse at 70% 38%, rgba(216,106,172,.6) 0, transparent 260px),
      linear-gradient(160deg, var(--plum) 0%, var(--plum-deep) 100%);
  }
  .edge-strip {
    position: absolute; left: 0; top: 210px;
    width: 22px; height: 150px;
    background: var(--lime);
  }
  .brand {
    position: absolute; left: 0; right: 0; top: 150px;
    text-align: center; color: var(--white);
    font-weight: 700; font-size: 88px; letter-spacing: 1px;
    line-height: 1;
  }
  .brand-mark {
    display: inline-block; width: 26px; height: 26px;
    border-radius: 50%; background: var(--white);
    vertical-align: middle; margin-right: 22px;
    position: relative; top: -10px;
  }
  .about {
    position: absolute; left: 300px; top: 280px; width: 560px;
    color: var(--white); text-transform: uppercase;
    font-size: 17px; line-height: 1.35; font-weight: 400;
    letter-spacing: .5px;
  }
  .about p + p { margin-top: 14px; }
  .about .savings {
    color: var(--lime); font-weight: 700; font-size: 22px;
  }
  .about .delivery { font-weight: 700; }
  .side-wedge {
    position: absolute; right: 0; top: 300px;
    width: 60px; height: 250px; background: var(--lime);
    clip-path: polygon(100% 0, 100% 100%, 0 100%, 40% 0);
  }
  .contact-banner {
    position: absolute; right: 0; top: 530px;
    width: 600px; height: 175px;
    background: var(--lime);
    clip-path: polygon(0 0, 100% 0, 100% 100%, 12% 100%, 12% 70%, 3% 70%, 11% 45%, 0 45%);
    padding: 38px 20px 0 110px;
    color: var(--ink-dark); font-weight: 700; font-size: 19px;
  }
  .contact-line { display: flex; align-items: center; gap: 16px; white-space: nowrap; }
  .contact-line + .contact-line { margin-top: 22px; }
  .contact-icon {
    width: 44px; height: 44px; flex: none;
    border: 2.5px solid var(--ink-dark); border-radius: 50%;
    display: flex; align-items: center; justify-content: center;
  }
  .website {
    position: absolute; left: 60px; bottom: 42px;
    color: var(--lime); font-weight: 700; font-size: 26px;
    text-transform: uppercase; letter-spacing: .5px;
  }
</style>
</head>
<body>
  <main class="postcard">
    <div class="backdrop-art" role="img" aria-label="Purple and pink painted background of an athlete lifting dumbbells, with a teal spray mark and yellow paint splatter"></div>
    <div class="edge-strip"></div>
    <div class="side-wedge"></div>

    <h1 class="brand"><span class="brand-mark"></span>The Motion Depot</h1>

    <section class="about">
      <p>The Motion Depot buys, sells and consigns gently used exercise equipment. Come in and find the right fit for your body and your budget!</p>
      <p>We offer treadmills, ellipticals, bikes, gyms and more, plus set-up, removal/recycling of old equipment and repair.</p>
      <p class="savings">Save up to 50% off of retail prices</p>
      <p class="delivery">We deliver! ~ Delivery available</p>
    </section>

    <section class="contact-banner">
      <div class="contact-line">
        <span class="contact-icon">
          <svg width="20" height="24" viewBox="0 0 20 24" fill="none" stroke="#4a3157" stroke-width="2.2">
            <path d="M10 22s7-7.5 7-13a7 7 0 0 0-14 0c0 5.5 7 13 7 13z"/>
            <circle cx="10" cy="9" r="2.6"/>
          </svg>
        </span>
        <span>4871 Birchwood Ave. NE Salem, Or 97305</span>
      </div>
      <div class="contact-line">
        <span class="contact-icon">
          <svg width="18" height="26" viewBox="0 0 18 26" fill="none" stroke="#4a3157" stroke-width="2.2">
            <rect x="2" y="2" width="14" height="22" rx="2.5"/>
            <line x1="7" y1="20" x2="11" y2="20"/>
          </svg>
        </span>
        <span>971-555-0187</span>
      </div>
    </section>

    <div class="website">www.themotiondepot.example</div>
  </main>
</body>
</html>
```